Business card - house cleaning company

We want friendly high end business card highlighting our services . NO LOGOs on back of card please.. no vertical cards NO DOUBLE BROOMS

2 owners of the company: Corinne Halvey & Joel Brandt

Included phone number: (555)318-2047

Email: brightlanetidy@mailnest.example

Website: www.brightlanetidy.example

Bonded & Insured

Larkmoor, CO 80999

Slogan maybe: Bringing a brighter shine to every corner of home

We want elegant high end card for house cleaning service. Maybe 2 sided if needed. Can it have bullet points of some services we offer

Residential Home Cleaning
Vacation Rental Cleaning
Commercial Cleaning
Carpet Cleaning
Window Cleaning
Property Management
Property Inspections
Property Maintenance
Trash Removal
Concierge Services

Highlight service on back of card. If we can do a one sided card with all this that’s great as well. Not cartoony.

Our logo attached and a design somone I had Perrin but they put very little time in. Not Unique enough. If you can do a custom design with a feminine touch that be great.

You will be eliminated for not reading the brief. NO DOUBLE LOGOS NO DOUBLE BROOMS. PLEASE BE CREATIVE. IF POST SAME LOGO WITH SMAL CHANGES RHEY WILL BE ELIMINATED. BE CREATIVE.

Thank you everyone for your designs. please only use the logo 1 time. and would love to see some that dont look all the same. We appreciate your time.

Target Market(s)

Residential and vacation rental home cleaning maid service

Industry/Entity Type

House cleaning maid services

Contact Information for Business Card

For business card use logo. black and green one provided. others for example. I wil try find some example.. We want friendly high end look. 2 owners of the company: Corinne Halvey & Joel Brandt Included phone number: (555)318-2047 Email: brightlanetidy@mailnest.example Website: www.brightlanetidy.example Bonded & Insured Estes Park, CO Slogan maybe: Bringing a brighter shine to every corner of home or Quality Service Guaranteed We want elegant high end card for house cleaning service. Maybe 2 sided if needed. Can it have bullet points of some services we offer Residential Home Cleaning Vacation Rental Cleaning Commercial Cleaning Carpet Cleaning Window Cleaning Property Management Property Inspections Property Maintenance Trash Removal Concierge Services

Requirements
Must have
• For business card use logo . Creativity. black and green one provided. We want friendly high end look. 2 owners of the company: Corinne Halvey & Joel Brandt Included phone number: (555)318-2047 Email: brightlanetidy@mailnest.example Website: www.brightlanetidy.example Licensed Bonded & Insured Estes Park, CO Slogan maybe: Bringing a brighter shine to every corner of home or Quality Service Guaranteed We want elegant high end card for house cleaning service. Maybe 2 sided if needed. Can it have bullet points of some services we offer Residential Home Cleaning Vacation Rental Cleaning Commercial Cleaning Carpet Cleaning Window Cleaning Property Management Property Inspections Property Maintenance Trash Removal Concierge Services .. creatitivty a plus. whimsical. we like stars..
Nice to have
• we want much better than the example of biz card provided as example. logo has colors that are in our website palette as well. We are open to ideas for the business card design. Will pay tip to best work. PLEASE USE COMPLIMENTING COLORS. . WE LIKE BLACK AND WHITE, stars
Should not have
• NO DOUBLE LOGOS. READ READ. READ. YOU WILL BE ELIMINATED no double logos or double brooms same side of card. I want didfrent examples. please don't make all your submission look the same

```html
<!DOCTYPE html>
<html lang="en">
<head>
<meta charset="utf-8">
<title>Bright Lane Tidy Services – Business Card</title>
<link href="https://fonts.googleapis.com/css2?family=Open+Sans:wght@400;600;700&display=swap" rel="stylesheet">
<style>
  :root {
    --backdrop: #2b2b2d;
    --card-blue: #2c6a93;
    --brand-blue: #245f8e;
    --leaf-green: #6b9a45;
    --ink-grey: #6d6e70;
    --paper: #ffffff;
    --tick-white: #ffffff;
  }
  html, body {
    margin: 0;
    padding: 0;
    width: 1200px;
    height: 979px;
    overflow: hidden;
    background: var(--backdrop);
    font-family: "Open Sans", Arial, sans-serif;
  }
  .stage {
    position: relative;
    width: 1200px;
    height: 979px;
  }
  .card {
    position: absolute;
    width: 680px;
    height: 390px;
    box-shadow: 0 18px 40px rgba(0,0,0,0.55);
    overflow: hidden;
  }
  /* Back side: services */
  .card-back {
    left: 150px;
    top: 60px;
    background: var(--card-blue);
    color: var(--tick-white);
  }
  .service-columns {
    position: absolute;
    left: 56px;
    top: 70px;
    right: 40px;
    display: flex;
    gap: 70px;
  }
  .service-list {
    list-style: none;
    margin: 0;
    padding: 0;
  }
  .service-list li {
    display: flex;
    align-items: center;
    gap: 18px;
    font-size: 13.5px;
    letter-spacing: 0.3px;
    text-transform: uppercase;
    line-height: 27px;
    white-space: nowrap;
  }
  .tick { width: 11px; height: 11px; flex: none; }
  .back-mark {
    position: absolute;
    right: 40px;
    bottom: 60px;
    font-size: 30px;
    font-weight: 600;
    color: rgba(255,255,255,0.08);
    letter-spacing: 0.5px;
  }

  /* Front side: contact */
  .card-front {
    left: 370px;
    top: 520px;
    background: var(--paper);
  }
  .brand {
    position: absolute;
    right: 40px;
    top: 44px;
    width: 300px;
    text-align: left;
  }
  .brand-name {
    display: flex;
    align-items: center;
    gap: 10px;
    font-size: 30px;
    font-weight: 700;
    color: var(--brand-blue);
    line-height: 1.1;
  }
  .brand-dot {
    width: 14px;
    height: 14px;
    border-radius: 50%;
    background: var(--leaf-green);
    flex: none;
  }
  .tagline {
    margin-top: 16px;
    font-size: 12px;
    font-weight: 700;
    color: var(--brand-blue);
    text-transform: uppercase;
    line-height: 1.6;
    letter-spacing: 0.2px;
  }
  .owners {
    position: absolute;
    left: 48px;
    top: 200px;
    font-size: 22px;
    font-weight: 700;
    color: var(--brand-blue);
  }
  .contact-list {
    position: absolute;
    left: 48px;
    top: 240px;
    list-style: none;
    margin: 0;
    padding: 0;
    color: var(--ink-grey);
    font-size: 14px;
    line-height: 22px;
  }
  .contact-list li {
    display: flex;
    align-items: center;
    gap: 9px;
  }
  .contact-icon { width: 13px; height: 13px; flex: none; }
  .contact-list .no-icon { padding-left: 22px; }
</style>
</head>
<body>
<main class="stage">

  <section class="card card-back" aria-label="Card back: services">
    <div class="service-columns">
      <ul class="service-list">
        <li><svg class="tick" viewBox="0 0 12 12"><path d="M1 6.5 L4.5 10 L11 1.5" fill="none" stroke="currentColor" stroke-width="1.4"/></svg>Residential Home Cleaning</li>
        <li><svg class="tick" viewBox="0 0 12 12"><path d="M1 6.5 L4.5 10 L11 1.5" fill="none" stroke="currentColor" stroke-width="1.4"/></svg>Vacation Rental Cleaning</li>
        <li><svg class="tick" viewBox="0 0 12 12"><path d="M1 6.5 L4.5 10 L11 1.5" fill="none" stroke="currentColor" stroke-width="1.4"/></svg>Commercial Cleaning</li>
        <li><svg class="tick" viewBox="0 0 12 12"><path d="M1 6.5 L4.5 10 L11 1.5" fill="none" stroke="currentColor" stroke-width="1.4"/></svg>Carpet Cleaning</li>
        <li><svg class="tick" viewBox="0 0 12 12"><path d="M1 6.5 L4.5 10 L11 1.5" fill="none" stroke="currentColor" stroke-width="1.4"/></svg>Window Cleaning</li>
      </ul>
      <ul class="service-list">
        <li><svg class="tick" viewBox="0 0 12 12"><path d="M1 6.5 L4.5 10 L11 1.5" fill="none" stroke="currentColor" stroke-width="1.4"/></svg>Property Management</li>
        <li><svg class="tick" viewBox="0 0 12 12"><path d="M1 6.5 L4.5 10 L11 1.5" fill="none" stroke="currentColor" stroke-width="1.4"/></svg>Property Inspections</li>
        <li><svg class="tick" viewBox="0 0 12 12"><path d="M1 6.5 L4.5 10 L11 1.5" fill="none" stroke="currentColor" stroke-width="1.4"/></svg>Property Maintenance</li>
        <li><svg class="tick" viewBox="0 0 12 12"><path d="M1 6.5 L4.5 10 L11 1.5" fill="none" stroke="currentColor" stroke-width="1.4"/></svg>Trash Removal</li>
        <li><svg class="tick" viewBox="0 0 12 12"><path d="M1 6.5 L4.5 10 L11 1.5" fill="none" stroke="currentColor" stroke-width="1.4"/></svg>Concierge Services</li>
      </ul>
    </div>
    <div class="back-mark">Bright Lane Tidy</div>
  </section>

  <section class="card card-front" aria-label="Card front: contact details">
    <div class="brand">
      <div class="brand-name"><span class="brand-dot"></span>Bright Lane Tidy</div>
      <p class="tagline">Bringing a brighter shine to<br>every corner of home</p>
    </div>

    <div class="owners">Corinne Halvey &amp; Joel Brandt</div>

    <ul class="contact-list">
      <li>
        <svg class="contact-icon" viewBox="0 0 14 14"><circle cx="7" cy="7" r="7" fill="#6b9a45"/><path d="M4.3 3.8 L5.6 3.6 L6.2 5.3 L5.4 6 Q6 7.6 7.9 8.6 L8.6 7.8 L10.3 8.4 L10.1 9.7 Q6.8 10.4 4.3 3.8Z" fill="#fff"/></svg>
        (555)318-2047
      </li>
      <li>
        <svg class="contact-icon" viewBox="0 0 14 14"><circle cx="7" cy="7" r="7" fill="#6b9a45"/><rect x="3.5" y="4.6" width="7" height="4.8" fill="none" stroke="#fff" stroke-width="1"/><path d="M3.5 4.6 L7 7.4 L10.5 4.6" fill="none" stroke="#fff" stroke-width="1"/></svg>
        brightlanetidy@mailnest.example
      </li>
      <li>
        <svg class="contact-icon" viewBox="0 0 14 14"><circle cx="7" cy="7" r="7" fill="#6b9a45"/><circle cx="7" cy="7" r="3.6" fill="none" stroke="#fff" stroke-width="0.9"/><ellipse cx="7" cy="7" rx="1.5" ry="3.6" fill="none" stroke="#fff" stroke-width="0.8"/><path d="M3.4 7 H10.6" stroke="#fff" stroke-width="0.8"/></svg>
        www.brightlanetidy.example
      </li>
      <li>
        <svg class="contact-icon" viewBox="0 0 14 14"><circle cx="7" cy="7" r="7" fill="#6b9a45"/><path d="M7 11 Q4 7.6 4 5.9 A3 3 0 0 1 10 5.9 Q10 7.6 7 11Z" fill="#fff"/><circle cx="7" cy="5.9" r="1.1" fill="#6b9a45"/></svg>
        Larkmoor, CO 80999
      </li>
      <li class="no-icon">Bonded &amp; Insured</li>
    </ul>
  </section>

</main>
</body>
</html>
```